Business Card and Letterhead for Nurlo - modern real estate business

I need a double sided business card design for Nurlo. Please see business card brief here https://papers.trelvimo.net/sheet/q/7XrTbaLeZpMmQ2uWvd9HkCj4yNoEfsGi3lRtAz_pk/view?mode=shared

Please feel free to design the business cards however you feel best. I am happy to give some creative freedoms and then provide feedback from there.

Please then also create a letterhead to match the business card design

Colors

Designer to choose colors to be used in the design.

Requirements
Must have
• Must be a modern, elegant business card which looks very professional

```html
<!DOCTYPE html>
<html lang="en">
<head>
<meta charset="utf-8">
<title>Nurlo Business Card</title>
<link rel="stylesheet" href="https://fonts.googleapis.com/css2?family=Montserrat:wght@400;500;600&display=swap">
<style>
  :root {
    --page-bg: #202020;
    --card-black: #060606;
    --brand-red: #e3202a;
    --text-white: #f4f4f4;
    --photo-dark: #1f2418;
    --photo-mid: #3b4229;
    --photo-light: #5a5f3c;
    --band-white: #ffffff;
  }
  * { box-sizing: border-box; margin: 0; padding: 0; }
  html, body { width: 1200px; height: 900px; overflow: hidden; }
  body {
    background: var(--page-bg);
    font-family: "Montserrat", sans-serif;
    color: var(--text-white);
    position: relative;
  }
  .card {
    position: absolute;
    left: 260px;
    width: 680px;
    height: 390px;
    overflow: hidden;
  }
  .card-front { top: 40px; background: var(--card-black); }
  .card-back { top: 470px; background: var(--card-black); }

  .front-wordmark {
    position: absolute;
    top: 120px; left: 0; right: 0;
    text-align: center;
    font-size: 112px;
    font-weight: 600;
    letter-spacing: 8px;
    color: var(--brand-red);
    line-height: 1;
  }
  .front-url {
    position: absolute;
    bottom: 34px; left: 0; right: 0;
    text-align: center;
    font-size: 16px;
    letter-spacing: 1.5px;
    color: var(--text-white);
  }
  .front-url .url-name { color: var(--brand-red); font-weight: 600; }

  .agent-photo {
    position: absolute; inset: 0;
    background:
      radial-gradient(ellipse 30% 55% at 50% 55%, #2a2a28 0%, transparent 70%),
      radial-gradient(ellipse 40% 50% at 80% 60%, var(--photo-light) 0%, transparent 70%),
      radial-gradient(ellipse 40% 50% at 15% 30%, var(--photo-mid) 0%, transparent 70%),
      linear-gradient(180deg, #3a3d34 0%, var(--photo-dark) 100%);
  }
  .photo-shade { position: absolute; inset: 0; background: rgba(0,0,0,0.45); }

  .back-wordmark {
    position: absolute;
    top: 42px; left: 0; right: 0;
    text-align: center;
    font-size: 76px;
    font-weight: 600;
    letter-spacing: 6px;
    color: var(--brand-red);
    line-height: 1;
  }
  .agent-id {
    position: absolute;
    top: 196px; right: 348px;
    text-align: right;
  }
  .agent-name {
    font-size: 27px;
    font-weight: 500;
    color: var(--brand-red);
    letter-spacing: 1px;
    line-height: 1.1;
  }
  .agent-title { font-size: 17px; color: var(--text-white); margin-top: 2px; }
  .id-divider {
    position: absolute;
    top: 192px; left: 345px;
    width: 1px; height: 86px;
    background: rgba(255,255,255,0.55);
  }
  .contact-list {
    position: absolute;
    top: 196px; left: 362px;
    list-style: none;
  }
  .contact-item {
    display: flex; align-items: center; gap: 10px;
    font-size: 18px; letter-spacing: 1px;
    height: 26px;
  }
  .contact-icon { width: 14px; height: 14px; flex: none; }
  .postal-address {
    position: absolute;
    top: 318px; left: 0; right: 0;
    text-align: center;
    font-size: 19px;
    letter-spacing: 1px;
  }
  .accent-band {
    position: absolute;
    left: 0; right: 0; bottom: 0;
    height: 11px;
    display: flex;
  }
  .accent-band .band-red { width: 66%; background: var(--brand-red); }
  .accent-band .band-white { flex: 1; background: var(--band-white); }
</style>
</head>
<body>
  <section class="card card-front" aria-label="Business card front">
    <div class="front-wordmark">NURLO</div>
    <p class="front-url">www.<span class="url-name">nurlo</span>.com</p>
  </section>

  <section class="card card-back" aria-label="Business card back">
    <div class="agent-photo" role="img" aria-label="Portrait photograph of the agent in a dark jacket against a blurred bushland backdrop"></div>
    <div class="photo-shade"></div>

    <div class="back-wordmark">NURLO</div>

    <div class="agent-id">
      <h1 class="agent-name">DANE HARLOW</h1>
      <p class="agent-title">Licenced Real Estate Agent</p>
    </div>
    <div class="id-divider"></div>

    <ul class="contact-list">
      <li class="contact-item">
        <svg class="contact-icon" viewBox="0 0 16 16" aria-hidden="true"><path fill="#e3202a" d="M3.6 1.2l2.3 2.6-1.4 1.9c.9 2 2.5 3.6 4.5 4.6l1.9-1.5 2.6 2.3-1.2 2.5C6.7 13.9 2 9.3 1.3 3.2z"/></svg>
        <span>0412 386 904</span>
      </li>
      <li class="contact-item">
        <svg class="contact-icon" viewBox="0 0 16 16" aria-hidden="true"><rect x="1.5" y="3.5" width="13" height="9" fill="none" stroke="#e3202a" stroke-width="1.4"/><path d="M1.5 3.8L8 9l6.5-5.2" fill="none" stroke="#e3202a" stroke-width="1.4"/></svg>
        <span>dane@nurlo.com</span>
      </li>
      <li class="contact-item">
        <svg class="contact-icon" viewBox="0 0 16 16" aria-hidden="true"><g fill="none" stroke="#e3202a" stroke-width="1.3"><circle cx="8" cy="8" r="6.3"/><ellipse cx="8" cy="8" rx="2.8" ry="6.3"/><path d="M1.7 8h12.6M2.8 4.8h10.4M2.8 11.2h10.4"/></g></svg>
        <span>www.nurlo.com</span>
      </li>
    </ul>

    <p class="postal-address">PO Box 1180 Larkvale NSW 2790</p>

    <div class="accent-band"><span class="band-red"></span><span class="band-white"></span></div>
  </section>
</body>
</html>
```